Sun Jubilee - Concert Poster

We need a poster for a concert involving 3 bands. Marmaduke, Auntie's Gumbo and Velveteen Ray. The event is called the Sun Jubilee. The poster will be a take away. We plan to print some to give out and some for advertising. Should be something people will want to put up on a wall. The poster should have a psychedelic "flavor", colorful.
Info. that needs to be on the poster: Sun Jubilee - Band Names - Pelham Brook's Music Hall - 4182 Route 17, Felton CA - $10 advance Tix - $12 at Door - for tickets www.pelhambrookmusic. - 21 and Over - March 21 2015 - Doors open at 7:00.

Industry/Entity Type

Event

```html
<!DOCTYPE html>
<html lang="en">
<head>
<meta charset="utf-8">
<title>Sun Jubilee – Concert Poster</title>
<link rel="stylesheet" href="https://fonts.googleapis.com/css2?family=Jost:wght@500;600&family=Permanent+Marker&display=swap">
<style>
  :root {
    --vermilion: #ff3300;
    --paint-green: #1fd11f;
    --plum: #7c0a80;
    --paper-white: #ffffff;
  }
  html, body {
    margin: 0;
    padding: 0;
    width: 776px;
    height: 1200px;
    overflow: hidden;
    background: var(--vermilion);
  }
  .poster { display: block; width: 776px; height: 1200px; }
  .backdrop { fill: var(--vermilion); }
  .paint-plum { fill: var(--plum); }
  .paint-green { fill: var(--paint-green); }
  .brush-type {
    font-family: "Permanent Marker", cursive;
    fill: var(--paper-white);
    text-transform: uppercase;
  }
  .brush-type--green { fill: var(--paint-green); }
  .info-type {
    font-family: "Jost", "Futura", sans-serif;
    font-weight: 600;
    fill: var(--paper-white);
    text-transform: uppercase;
  }
  .info-type--date { font-weight: 500; }
</style>
</head>
<body>
<svg class="poster" viewBox="0 0 776 1200" xmlns="http://www.w3.org/2000/svg">
  <rect class="backdrop" width="776" height="1200"/>

  <g class="paint-strokes" role="img" aria-label="Loose psychedelic brush strokes in green and plum over a vermilion field">
    <path class="paint-plum" d="M0 0 H170 C150 60 120 110 150 170 C170 220 120 250 80 240 C40 230 20 200 0 210 Z"/>
    <path class="paint-plum" d="M560 400 C640 380 720 430 760 500 C780 560 740 640 700 700 C680 760 720 820 700 880 C680 940 620 980 580 1000 L560 960 C600 900 600 840 620 780 C640 700 600 640 580 560 C570 500 540 450 560 400 Z"/>
    <path class="paint-plum" d="M0 900 C80 880 160 920 220 980 C260 1030 300 1100 280 1200 H0 Z"/>
    <path class="paint-plum" d="M520 980 C600 960 680 1000 700 1060 C720 1120 660 1180 600 1200 H500 C540 1140 480 1060 520 980 Z"/>

    <path class="paint-green" d="M118 32 L640 26 L648 120 L628 210 L650 300 L612 340 L585 392 L600 452 L470 470 L330 462 L210 480 L142 450 L125 360 L110 250 L128 150 Z"/>
    <path class="paint-green" d="M480 400 C540 380 600 390 630 410 L600 440 C560 420 520 420 480 430 Z"/>
    <path class="paint-green" d="M160 470 L320 462 L340 560 L300 650 L330 760 L290 900 L180 905 L150 780 L175 660 L150 560 Z"/>
    <path class="paint-green" d="M160 880 L560 870 L575 940 L540 1010 L420 1030 L170 1020 L150 950 Z"/>
    <path class="paint-green" d="M420 1020 L650 1010 L640 1070 L600 1095 L430 1085 Z"/>
    <path class="paint-green" d="M118 1090 L650 1068 L644 1128 L126 1142 Z"/>
  </g>

  <g class="lineup">
    <text class="brush-type" x="384" y="122" font-size="84" text-anchor="middle" textLength="440" lengthAdjust="spacingAndGlyphs">Marmaduke</text>
    <text class="brush-type" x="384" y="210" font-size="66" text-anchor="middle" textLength="520" lengthAdjust="spacingAndGlyphs">Auntie's Gumbo</text>
    <text class="brush-type" x="384" y="298" font-size="66" text-anchor="middle" textLength="520" lengthAdjust="spacingAndGlyphs">Velveteen Ray</text>
  </g>

  <g class="date-block">
    <text class="info-type info-type--date" x="188" y="396" font-size="40" letter-spacing="6">March 21 2015</text>
    <text class="info-type info-type--date" x="188" y="444" font-size="28" letter-spacing="4">Doors open 7:00<tspan text-transform="none">pm</tspan></text>
  </g>

  <g class="event-title">
    <text class="brush-type" x="390" y="660" font-size="230" text-anchor="middle" textLength="460" lengthAdjust="spacingAndGlyphs">Sun</text>
    <text class="brush-type" x="388" y="858" font-size="190" text-anchor="middle" textLength="600" lengthAdjust="spacingAndGlyphs">Jubilee</text>
  </g>

  <g class="event-details">
    <text class="info-type" x="176" y="903" font-size="22" letter-spacing="1.5" textLength="394" lengthAdjust="spacingAndGlyphs">$10 Advance Tix/$12 at Door</text>
    <text class="info-type" x="176" y="950" font-size="22" letter-spacing="2" textLength="394" lengthAdjust="spacingAndGlyphs">Pelham Brook's Music Hall</text>
    <text class="info-type" x="176" y="996" font-size="22" letter-spacing="2" textLength="394" lengthAdjust="spacingAndGlyphs">4182 Route 17, Felton CA</text>
    <text class="info-type" x="176" y="1057" font-size="26" letter-spacing="2">21 and over</text>
    <text class="brush-type brush-type--green" x="424" y="1048" font-size="34" textLength="214" lengthAdjust="spacingAndGlyphs">For tickets:</text>
    <text class="brush-type" x="384" y="1124" font-size="38" text-anchor="middle" textLength="480" lengthAdjust="spacingAndGlyphs">www.pelhambrookmusic.com</text>
  </g>
</svg>
</body>
</html>
```